Seeking funky, innovative business cards

I am looking to refresh our current business cards to something more engaging, visual and impactful. We are a management consultancy firm, see website (www.larkspur-advisory.com.au). I've included our colour scheme, sample of the slides we use and our old business cards. We would like our cards to have icons. The card should display:- Name- Title- Mobile number- Address- Email address- Website - Company logo- Our purpose statement "We shape workplaces people are proud to join"

Contact Information for Business Card

Tavish Brellan
Consultant
0491 672 348
Level 5, 218 Warrick Lane, Melbourne 3000
tavish@larkspur-advisory.com.au
www.larkspur-advisory.com.au

Purpose statement "We shape workplaces people are proud to join"
LOGO available in google images

Font styles to use
Other font styles liked:
• Open Sans Light, Bebas Neue (open to other cool foints)

Colors
ffc214
5c5c5c
f5f5f5
fefefe

Requirements
Must have
• - Name
• - Title
• - Mobile number
• - Address
• - Email address
• - Website
• - Company logo
• - Our purpose statement "We shape workplaces people are proud to join"
Nice to have
• - Icons
• - Colour (see our colour scheme"

```html
<!DOCTYPE html>
<html lang="en">
<head>
<meta charset="utf-8">
<title>Larkspur Advisory – Business Cards</title>
<link rel="stylesheet" href="https://fonts.googleapis.com/css2?family=Open+Sans:wght@300;400;700;800&display=swap">
<style>
  :root {
    --yellow: #ffc214;
    --yellow-light: #f7d63a;
    --yellow-deep: #e3b40f;
    --grey: #5c5c5c;
    --grey-dark: #3f4244;
    --paper: #f5f5f5;
    --white: #fefefe;
    --stage: #d9d9d9;
  }
  * { box-sizing: border-box; margin: 0; padding: 0; }
  html, body {
    width: 1200px; height: 900px; overflow: hidden;
    background: var(--stage);
    font-family: "Open Sans", Arial, sans-serif;
  }
  .canvas {
    width: 1200px; height: 900px;
    display: flex; flex-direction: column; align-items: center; justify-content: center;
    gap: 40px;
  }
  .card {
    position: relative;
    width: 620px; height: 379px;
    overflow: hidden;
    box-shadow: 0 10px 28px rgba(0,0,0,.22);
  }

  /* Back side */
  .card--back {
    background: linear-gradient(160deg, var(--yellow-deep) 0%, var(--yellow) 55%, var(--yellow-light) 100%);
    color: var(--white);
    display: flex; flex-direction: column; align-items: center;
  }
  .card--back .wordmark { margin-top: 118px; }
  .card--back .wordmark__name { color: var(--white); font-size: 68px; }
  .card--back .wordmark__sub { color: var(--white); }
  .purpose {
    position: absolute; bottom: 54px; left: 0; right: 0;
    text-align: center;
    font-weight: 700; font-size: 13px; letter-spacing: .6px;
    text-transform: uppercase; color: var(--white);
  }

  /* Wordmark */
  .wordmark { display: flex; flex-direction: column; align-items: flex-end; }
  .wordmark__name {
    font-weight: 300; font-size: 62px; line-height: 1; letter-spacing: -1px;
    color: var(--grey);
  }
  .wordmark__sub {
    font-weight: 400; font-size: 12px; letter-spacing: 4px;
    text-transform: uppercase; color: var(--grey); margin-top: 4px;
  }

  /* Front side */
  .card--front { background: var(--paper); color: var(--grey); }
  .card--front .wordmark { position: absolute; top: 44px; left: 42px; }
  .holder { position: absolute; top: 178px; left: 42px; right: 42px; }
  .holder__name {
    font-weight: 800; font-size: 19px; letter-spacing: .4px;
    text-transform: uppercase; color: var(--yellow);
  }
  .holder__title-row { display: flex; align-items: center; gap: 10px; }
  .holder__title { font-size: 14px; color: var(--grey); }
  .holder__rule { flex: 1; height: 1px; background: var(--grey); margin-top: 4px; }
  .contacts {
    position: absolute; top: 238px; left: 42px;
    list-style: none; font-size: 14px; line-height: 21px; color: var(--grey);
  }
  .contacts li { display: flex; align-items: center; gap: 9px; }
  .contacts svg { width: 12px; height: 12px; flex: none; }
  .address {
    position: absolute; right: 42px; bottom: 48px;
    text-align: right; font-size: 14.5px; line-height: 20px; color: var(--grey);
    font-style: normal;
  }
  .band { position: absolute; bottom: 0; }
  .band--dark { left: 0; width: 270px; height: 22px; background: var(--grey-dark); }
  .band--accent { left: 278px; right: 0; height: 10px; background: var(--yellow); }
</style>
</head>
<body>
<main class="canvas">
  <section class="card card--back" aria-label="Card back">
    <div class="wordmark">
      <span class="wordmark__name">Larkspur</span>
      <span class="wordmark__sub">Advisory</span>
    </div>
    <p class="purpose">We shape workplaces people are proud to join</p>
  </section>

  <section class="card card--front" aria-label="Card front">
    <div class="wordmark">
      <span class="wordmark__name">Larkspur</span>
      <span class="wordmark__sub">Advisory</span>
    </div>

    <div class="holder">
      <h1 class="holder__name">Tavish Brellan</h1>
      <div class="holder__title-row">
        <span class="holder__title">Consultant</span>
        <span class="holder__rule"></span>
      </div>
    </div>

    <ul class="contacts">
      <li>
        <svg viewBox="0 0 12 12" aria-hidden="true"><path d="M2.5 1 L4.5 1 L5.3 3.5 L4 4.6 C4.7 6 5.9 7.2 7.4 8 L8.5 6.7 L11 7.5 L11 9.5 C11 10.3 10.3 11 9.5 11 C5 11 1 7 1 2.5 C1 1.7 1.7 1 2.5 1 Z" fill="var(--yellow)"/></svg>
        0491 672 348
      </li>
      <li>
        <svg viewBox="0 0 12 12" aria-hidden="true"><rect x="1" y="2.5" width="10" height="7" fill="none" stroke="var(--yellow)" stroke-width="1.2"/><path d="M1 2.5 L6 6.5 L11 2.5" fill="none" stroke="var(--yellow)" stroke-width="1.2"/></svg>
        tavish@larkspur-advisory.com.au
      </li>
      <li>
        <svg viewBox="0 0 12 12" aria-hidden="true"><circle cx="6" cy="6" r="5" fill="none" stroke="var(--yellow)" stroke-width="1.2"/><ellipse cx="6" cy="6" rx="2.2" ry="5" fill="none" stroke="var(--yellow)" stroke-width="1"/><path d="M1 6 H11" stroke="var(--yellow)" stroke-width="1"/></svg>
        www.larkspur-advisory.com.au
      </li>
    </ul>

    <address class="address">
      Level 5, 218 Warrick Lane<br>
      Melbourne 3000
    </address>

    <span class="band band--dark"></span>
    <span class="band band--accent"></span>
  </section>
</main>
</body>
</html>
```